No logos or construction designs

Easy to read Carl Wexford Roofing, LLC (in red)

all other lettering in black I guess I am open to what the designers come up

Construction

Carl Wexford Roofing, LLC office 555-2918463 fax 555-813-904 3875 Tamarind Ave W Larkfield, Ohio 44690
Carl@CarlWexfordRoofing.example Residential Commerical
Carl Wexford cell 555-362-1187

```html
<!DOCTYPE html>
<html lang="en">
<head>
<meta charset="utf-8">
<title>Carl Wexford Roofing, LLC – Business Card</title>
<link rel="stylesheet" href="https://fonts.googleapis.com/css2?family=Cinzel:wght@600;700;800&display=swap">
<style>
  :root {
    --band-grey: #636466;
    --brand-red: #d3202f;
    --ink-grey: #5f6062;
    --paper: #ffffff;
  }
  * { margin: 0; padding: 0; box-sizing: border-box; }
  html, body {
    width: 1200px;
    height: 692px;
    overflow: hidden;
    background: var(--paper);
  }
  .card {
    position: relative;
    width: 1200px;
    height: 692px;
    background: var(--paper);
    font-family: "Cinzel", "Times New Roman", serif;
    font-weight: 700;
    font-style: normal;
    color: var(--ink-grey);
  }
  .header-band {
    position: absolute;
    left: 0; top: 0;
    width: 1200px;
    height: 192px;
    background: var(--band-grey);
  }
  .company-name,
  .owner-name {
    position: absolute;
    left: 58px;
    color: var(--brand-red);
    font-size: 50px;
    line-height: 1;
    letter-spacing: 2px;
    white-space: nowrap;
  }
  .company-name { top: 44px; }
  .owner-name { top: 114px; }

  .mailing-address { font-style: normal; }

  .services,
  .address-line {
    position: absolute;
    left: 60px;
    font-size: 40px;
    font-style: normal;
    line-height: 1;
    letter-spacing: 2px;
    white-space: nowrap;
  }
  .services { top: 230px; }
  .address-street { top: 316px; }
  .address-city { top: 388px; }

  .email {
    position: absolute;
    left: 0;
    width: 1200px;
    top: 500px;
    text-align: center;
    font-size: 38px;
    line-height: 1;
    letter-spacing: 2px;
    white-space: nowrap;
  }

  .contact-row {
    position: absolute;
    left: 0;
    top: 578px;
    width: 1200px;
    height: 72px;
  }
  .contact-item {
    position: absolute;
    top: 0;
    width: 394px;
    text-align: center;
    white-space: nowrap;
  }
  .contact-item.cell { left: 9px; }
  .contact-item.fax { left: 403px; }
  .contact-item.office { left: 799px; }
  .contact-label {
    display: block;
    font-size: 30px;
    line-height: 30px;
    letter-spacing: 3px;
  }
  .contact-number {
    display: block;
    font-size: 36px;
    line-height: 40px;
    letter-spacing: 3px;
  }
  .divider {
    position: absolute;
    top: 0;
    width: 4px;
    height: 70px;
    background: var(--ink-grey);
  }
  .divider.first { left: 404px; }
  .divider.second { left: 788px; }
</style>
</head>
<body>
  <main class="card">
    <div class="header-band">
      <div class="company-name">Carl Wexford Roofing, LLC</div>
      <div class="owner-name">Carl Wexford</div>
    </div>

    <div class="services">Residential / Commerical</div>

    <address class="mailing-address">
      <div class="address-line address-street">3875 Tamarind Ave W</div>
      <div class="address-line address-city">Larkfield, Ohio 44690</div>
    </address>

    <div class="email">Carl@CarlWexfordRoofing.example</div>

    <div class="contact-row">
      <div class="contact-item cell">
        <span class="contact-label">cell</span>
        <span class="contact-number">555-362-1187</span>
      </div>
      <div class="divider first"></div>
      <div class="contact-item fax">
        <span class="contact-label">fax</span>
        <span class="contact-number">555-813-904</span>
      </div>
      <div class="divider second"></div>
      <div class="contact-item office">
        <span class="contact-label">office</span>
        <span class="contact-number">555-291-8463</span>
      </div>
    </div>
  </main>
</body>
</html>
```